Corvane Electrical Solutions

On one side. LOGO (underneath:) Commercial Industrial Residential

- NAME & CONTACT DETAILS

Marcus T. Hollings
Project Manager

(Cell icon) (441) 582-6197
(Email icon) cvnelectricalsoultions@mailventra.com
(Facebook & Instagram icons )@cvnelectricalsolutions

Other side: LOGO - underneath ELECTRICAL CONSTRUCTION & MAINTENANCE . LED LIGHTING & AUTOMATION . LIFE SAFETY SYSTEMS (FIRE ALARM / SECURITY) . DATA & COMMUNICATION

```html
<!DOCTYPE html>
<html lang="en">
<head>
<meta charset="utf-8">
<title>Corvane Electrical Solutions — Business Card</title>
<link rel="stylesheet" href="https://fonts.googleapis.com/css2?family=Arimo:wght@400;700&display=swap">
<style>
  :root {
    --page-bg: #2b2b2d;
    --card-white: #ffffff;
    --card-shade: #eceeef;
    --teal: #1c5b6c;
    --teal-dark: #164b59;
    --ink: #4a4a4a;
    --rule: #5a5a5a;
    --band-text: #e6eef0;
  }
  * { box-sizing: border-box; margin: 0; padding: 0; }
  html, body {
    width: 1200px; height: 997px; overflow: hidden;
    background: var(--page-bg);
    font-family: "Arimo", Arial, sans-serif;
  }
  .sheet {
    position: relative; width: 1200px; height: 997px;
    display: flex; flex-direction: column; align-items: center; justify-content: center; gap: 56px;
  }
  .card {
    position: relative; width: 700px; height: 400px;
    background: linear-gradient(135deg, var(--card-white) 0%, var(--card-shade) 100%);
    box-shadow: 0 14px 30px rgba(0,0,0,.45);
    overflow: hidden;
  }
  .card__rule {
    position: absolute; left: 0; right: 0; bottom: 74px; height: 4px; background: var(--rule);
  }
  .card__band {
    position: absolute; left: 0; right: 0; bottom: 0; height: 62px;
    background: var(--teal);
    display: flex; align-items: center; justify-content: center;
    color: var(--band-text); font-size: 17px; letter-spacing: .06em; text-transform: uppercase;
  }
  .wordmark {
    display: flex; align-items: center; gap: 14px;
  }
  .wordmark__square {
    width: 34px; height: 34px; background: var(--teal);
  }
  .wordmark__name {
    color: var(--teal); font-weight: 700; font-size: 34px; letter-spacing: .04em;
    text-transform: uppercase; line-height: 1;
  }
  /* back side */
  .card--back .wordmark { position: absolute; left: 0; right: 0; top: 66px; justify-content: center; }
  .services {
    position: absolute; left: 0; right: 0; top: 150px;
    list-style: none; text-align: center;
    color: var(--teal); font-size: 15px; letter-spacing: .05em; line-height: 1.75; text-transform: uppercase;
  }
  /* front side */
  .card--front .wordmark { position: absolute; left: 0; right: 0; top: 72px; justify-content: center; }
  .identity {
    position: absolute; top: 168px; left: 60px; width: 250px; height: 110px;
    display: flex; flex-direction: column; justify-content: flex-end; align-items: flex-end; text-align: right;
  }
  .identity__name { color: var(--teal); font-weight: 700; font-size: 22px; letter-spacing: .03em; text-transform: uppercase; }
  .identity__role { color: var(--ink); font-size: 16px; margin-top: 2px; }
  .divider {
    position: absolute; top: 168px; left: 330px; width: 3px; height: 116px; background: var(--rule);
  }
  .contacts {
    position: absolute; top: 170px; left: 350px; list-style: none;
    color: var(--ink); font-size: 14.5px;
  }
  .contacts li { display: flex; align-items: center; gap: 9px; height: 26px; }
  .contacts svg { width: 17px; height: 17px; flex: none; }
</style>
</head>
<body>
<main class="sheet">

  <section class="card card--back" aria-label="Card back">
    <div class="wordmark">
      <span class="wordmark__square"></span>
      <span class="wordmark__name">Corvane Electrical Solutions</span>
    </div>
    <ul class="services">
      <li>Electrical Construction &amp; Maintenance</li>
      <li>LED Lighting &amp; Automation</li>
      <li>Life Safety Systems (Fire Alarm / Security)</li>
      <li>Data &amp; Communication</li>
    </ul>
    <div class="card__rule"></div>
    <div class="card__band">Commercial Industrial Residential</div>
  </section>

  <section class="card card--front" aria-label="Card front">
    <div class="wordmark">
      <span class="wordmark__square"></span>
      <span class="wordmark__name">Corvane Electrical Solutions</span>
    </div>

    <div class="identity">
      <p class="identity__name">Marcus T. Hollings</p>
      <p class="identity__role">Project Manager</p>
    </div>
    <div class="divider"></div>

    <ul class="contacts">
      <li>
        <svg viewBox="0 0 20 20" aria-hidden="true"><circle cx="10" cy="10" r="10" fill="#1c5b6c"/><path d="M6.5 5.5h2l1 2.5-1.3 1a6 6 0 0 0 2.8 2.8l1-1.3 2.5 1v2a1 1 0 0 1-1 1A8.5 8.5 0 0 1 5.5 6.5a1 1 0 0 1 1-1z" fill="#fff"/></svg>
        (441) 582-6197
      </li>
      <li>
        <svg viewBox="0 0 20 20" aria-hidden="true"><circle cx="10" cy="10" r="10" fill="#1c5b6c"/><rect x="5" y="6.5" width="10" height="7" fill="#fff"/><path d="M5 6.5l5 4 5-4" fill="none" stroke="#1c5b6c" stroke-width="1.2"/></svg>
        cvnelectricalsoultions@mailventra.com
      </li>
      <li>
        <svg viewBox="0 0 20 20" aria-hidden="true"><circle cx="10" cy="10" r="10" fill="#1c5b6c"/></svg>
        @cvnelectricalsolutions
      </li>
      <li>
        <svg viewBox="0 0 20 20" aria-hidden="true"><circle cx="10" cy="10" r="10" fill="#1c5b6c"/></svg>
        @cvnelectricalsolutions
      </li>
    </ul>

    <div class="card__rule"></div>
    <div class="card__band">Commercial Industrial Residential</div>
  </section>

</main>
</body>
</html>
```